Flyer-Design für Physiotherapie-Praxis
Zielgruppe
Wir sind eine Praxis für Physiotherapie und möchten durch diesen Flyer neue Patienten werben. Der Flyer soll in Arztpraxen ausliegen und dort den Patienten direkt ansprechen und auf uns aufmerksam machen. Es ist auch eine Verknüpfung der Therapie mit einem Training in einem Gesundheitsstudio möglich, da im gleichen Haus das Physio Kraftwerk Eichenstetten beheimatet ist.
Aufgabenstellung
Der Fokus auf unsere Prinzipien (Ganzheitliche Therapie, hohes Maß an Therapiemöglichkeiten, Variation in den therapeutischen Ansätzen durch unterschiedlich fortgebildete Therapeuten, die nach den gleichen Idealen arbeiten)

```html
<!DOCTYPE html>
<html lang="de">
<head>
<meta charset="utf-8">
<title>Flyer Zentrum für Therapie &amp; Training</title>
<link href="https://fonts.googleapis.com/css2?family=Source+Sans+3:wght@300;400;600;700&display=swap" rel="stylesheet">
<style>
:root{
  --blue:#1b95d2;
  --navy:#2b2c5e;
  --lime:#b6cc35;
  --white:#ffffff;
  --photo-team:#8fb9d6;
  --photo-pool:#7fc0d8;
  --photo-gym:#b9b4ac;
}
*{margin:0;padding:0;box-sizing:border-box}
html,body{width:1200px;height:1200px;overflow:hidden;background:var(--white)}
body{position:relative;font-family:"Source Sans 3",sans-serif;font-weight:300}
.panel{position:absolute;top:67px;width:511px;height:1073px;overflow:hidden;box-shadow:0 3px 10px rgba(0,0,0,.25)}
.panel--front{left:69px;background:var(--white)}
.panel--inside{left:628px;background:var(--white)}
.wave{position:absolute;left:0;top:0;width:511px;height:1073px}
.photo{position:absolute}
.brand{position:absolute;top:30px;left:0;width:100%;text-align:center;color:var(--navy);font-weight:400}
.brand__mark{width:110px;height:110px;border:2px solid var(--navy);border-radius:50%;margin:0 auto 22px}
.brand__line{font-size:19px;letter-spacing:1px;line-height:1.1}
.brand__name{font-size:27px;line-height:1.2}
.brand__owner{font-size:17px;line-height:1.2}
.badge{position:absolute;width:128px;height:128px;border-radius:50%;background:var(--lime);color:var(--white);display:flex;flex-direction:column;align-items:center;justify-content:center;text-align:center;font-size:13.5px;line-height:1.2;transform:rotate(-8deg)}
.badge b{font-weight:700}
.headline{position:absolute;left:65px;width:381px;color:var(--white);line-height:1}
.headline__light{font-size:37px;font-weight:300;letter-spacing:-.5px;display:block}
.headline__bold{font-size:39px;font-weight:700;display:block;margin-top:2px}
.body{position:absolute;text-align:justify;font-size:13px;line-height:17.3px}
.body b{font-weight:700}
.front-body{left:65px;top:790px;width:381px;color:var(--white)}
.rule{position:absolute;left:65px;top:977px;width:381px;height:1.5px;background:var(--white)}
.footer{position:absolute;left:65px;top:988px;width:381px;color:var(--white);font-size:11.5px;line-height:17px;text-align:justify}
.footer b{font-weight:700}
.section-title{position:absolute;color:var(--white);line-height:1}
.section-title .light{display:block;font-size:24px;font-weight:300}
.section-title .bold{display:block;font-size:24px;font-weight:700;margin-top:2px}
.section-title--right{right:46px;text-align:right;color:var(--blue)}
.inside-body-1{left:46px;top:110px;width:418px;color:var(--white);font-size:12.6px}
.inside-body-2{left:46px;top:649px;width:418px;color:var(--blue);font-size:12.6px}
.inside-rule{position:absolute;left:0;top:1052px;width:511px;height:1.5px;background:var(--blue)}
</style>
</head>
<body>

<section class="panel panel--front">
  <div class="brand">
    <div class="brand__mark"></div>
    <div class="brand__line">ZENTRUM FÜR THERAPIE &amp; TRAINING</div>
    <div class="brand__name">Holger Brandt &amp; Karin Seidel</div>
    <div class="brand__owner">Inhaber: Karin Seidel</div>
  </div>
  <div class="photo" role="img" aria-label="Teamfoto der Therapeutinnen und Therapeuten in hellblauen Poloshirts" style="left:0;top:260px;width:511px;height:420px;background:linear-gradient(180deg,#6f8fae 0%,var(--photo-team) 45%,#c9dceb 100%)"></div>
  <svg class="wave" viewBox="0 0 511 1073" aria-hidden="true">
    <path d="M0,612 C100,655 220,652 330,600 C400,568 455,570 511,618 L511,1073 L0,1073 Z" fill="var(--blue)"/>
    <path d="M0,612 C100,640 220,640 330,585 C400,555 455,558 511,604" fill="none" stroke="var(--white)" stroke-width="1.5"/>
  </svg>
  <div class="badge" style="left:382px;top:545px"><b>Seit über</b><b>50 Jahren -</b>ein Zeichen für<br>Qualität und<br>Vertrauen</div>
  <h1 class="headline" style="top:706px">
    <span class="headline__light">WIR SIND THERAPEUTEN</span>
    <span class="headline__bold">AUS ÜBERZEUGUNG!</span>
  </h1>
  <p class="body front-body"><b>Unsere Praxis gibt es seit 1969. In dieser Zeit konnten wir viel Erfahrung sammeln.</b> Wir sind ein Team aus älteren und jüngeren Therapeuten, aus Masseuren, med. Bademeistern und Physiotherapeuten. Diese bunte Mischung beinhaltet viel Erfahrung und viel Wissen. Beides wird in regelmäßigen internen Fortbildungen ausgetauscht. So ergänzen wir uns gegenseitig. Wir arbeiten als Team Hand in Hand und schätzen das Fachwissen jedes einzelnen Kollegen. Wir sind motiviert und mit Freude bei der Arbeit, denn wir wissen, was unsere Patienten mit Hilfe der Physiotherapie erreichen können.</p>
  <div class="rule"></div>
  <p class="footer"><b>Zentrum für Therapie und Training Holger Brandt &amp; Karin Seidel</b><br><b>Inhaber: Karin Seidel</b> • Lindenweg 27 • 90681 Eichenstetten<br>Telefon: 0911-486209 • Telefax: 0911-4862099 • termine@praxis-brandt.de</p>
</section>

<section class="panel panel--inside">
  <svg class="wave" viewBox="0 0 511 1073" aria-hidden="true">
    <path d="M0,0 L511,0 L511,503 C440,490 370,520 280,562 C180,605 80,600 0,570 Z" fill="var(--blue)"/>
  </svg>
  <h2 class="section-title" style="left:46px;top:47px"><span class="light">VIELEZAHL VON</span><span class="bold">THERAPIEMÖGLICHKEITEN</span></h2>
  <p class="body inside-body-1">Wir haben eine <b>Vielzahl von Therapiegeräten</b> und -hilfsmitteln zur Verfügung, z.B. eine Kletterwand, Sling Trainer, eine Vibrano®-Rüttelplatte, ein Slack Rack und ein <b>Bewegungsbad!</b> Im 32°C warmem Wasser können sich unsere Patienten besser bewegen. Mit unserem Fachwissen und unserer Erfahrung haben wir uns auf die Behandlung orthopädischer, chirurgischer und neurologischer Patienten spezialisiert.</p>
  <div class="photo" role="img" aria-label="Bewegungsbad mit Handläufen und Pflanzen im Wintergarten" style="left:46px;top:229px;width:418px;height:278px;background:linear-gradient(180deg,#e6ecec 0%,#7fa37a 40%,var(--photo-pool) 65%,#9a958c 100%)"></div>
  <svg class="wave" viewBox="0 0 511 1073" aria-hidden="true">
    <path d="M0,570 C80,600 180,605 280,562 C370,520 440,490 511,503 L511,1073 L0,1073 Z" fill="var(--white)"/>
    <path d="M0,525 C80,560 170,560 260,515 C350,470 440,445 511,455" fill="none" stroke="var(--white)" stroke-width="1.5"/>
  </svg>
  <div class="badge" style="left:247px;top:444px;transform:rotate(10deg)">WIR HABEN<br><span><b>DAS ZIEL</b>, ZU DEN</span>BESTEN UNSERES<br>FACHS ZU<br>GEHÖREN</div>
  <h2 class="section-title section-title--right" style="top:579px"><span class="light">AKTIVES</span><span class="bold">GESUNDHEITSTRAINING</span></h2>
  <p class="body inside-body-2">Für gute Fortschritte in der Therapie und die Erhaltung dieser Fortschritte ist der Weg zur sportlichen Aktivität essentiell. Diesen Weg erleichtern wir unseren Patienten durch unser Angebot des <b>Aktiven Gesundheitstrainings</b>. Zusätzlich zu Ihrem Rezept erhalten unsere neuen Patienten einen zusätzlichen und kostenfreien Beratungstermin im Physio Kraftwerk Eichenstetten. In diesem Termin zeigen wir Ihnen Möglichkeiten, selbst etwas zu Ihrer Gesundung beizutragen. Je nachdem, was Ihnen gerade am effektivsten hilft, trainieren Sie 6 x am Kraft-Ausdauer-Zirkel der Firma Fortivo oder am motiflex-Zirkel. Das Training an diesen Geräten ist einfach, sicher und effektiv. Da das Training maximal 35 Minuten Zeit beansprucht ist Zeitmangel kein Argument mehr.</p>
  <div class="photo" role="img" aria-label="Trainingsraum mit Kraft- und Ausdauergeräten" style="left:46px;top:849px;width:418px;height:184px;background:linear-gradient(180deg,#f0ebe0 0%,var(--photo-gym) 50%,#8e8c88 100%)"></div>
  <div class="inside-rule"></div>
</section>

</body>
</html>
```